New Website for Crime Scene Cleaner required

I need someone to create a complete new website and can set up SEO for me through the Website Designer or a third party for me. I have Logo that i will upload shortly once finalized for the website. I have domain names already but will need to be registered by the winner(i can supply the details I have received from HostMarlo). I am looking for a website that stands out but is simple and elegant, easy to navigate and use yet not boring. Using information provided by me for wording to create it as a stand out website. in total i am looking at 5-7 pages (About/Home, Fire & Smoke Restoration, Water Restoration/Mould Remediation, Crime Scene Cleaners, Methamphetamine Remediation/ Testing Services, Hoarding & Squalor Cleaning, Contact Us/Testimonials)This will be a start to finish project. I would like assistance to have it set up user friendly on mobile devices etc or refer a third party who can assist. Must be able to provide ongoing support when required by myself if the successful winner (i understand this will be an additional fee if required in the future).
You will also require to assist me with the email set up for the website so that it is fully functional or provide a third party who can.
To gain some information about the business you can visit my old website at www.pelbrookcove.com.au and welcome to use some of the wording from there for your entry.
It's been 14yrs since i've had a website made from me so suggestions are welcome if not mentioned in the scope as I want the website to be great.

I have uploaded 2 Logo's and a 3D Logo will come through shortly.

Target Market(s)

People affected by a traumatic event in their lives needing assistance by professionals who are understanding and professionally trained

Coding

Coded - Design and coding required

Requirements
Must have
• *** Please note that correct wording for pages will only be supplied upon a successful winner for the finalization of the project.

I have domain names already but will need to be registered by the winner(i can supply the details I have received from HostMarlo).
Nice to have
• the feeling that we care because we do and that we are passionate for what we do.

```html
<!DOCTYPE html>
<html lang="en">
<head>
<meta charset="utf-8">
<title>Haven &amp; Clear Services</title>
<link rel="stylesheet" href="https://fonts.googleapis.com/css2?family=Lato:wght@400;700&display=swap">
<style>
:root{
  --orange:#e8441f;
  --orange-light:#f0701a;
  --orange-mid:#ec5a1d;
  --text:#222;
  --muted:#555;
  --white:#fff;
  --dark:#1d1d1d;
  --footer-text:#9a9a9a;
  --sky:#3d6fb8;
  --hero-title:#c4dcf5;
}
*{box-sizing:border-box;margin:0;padding:0}
html,body{width:1200px;height:3686px;overflow:hidden}
body{position:relative;font-family:'Lato',sans-serif;color:var(--text);background:var(--white)}
.abs{position:absolute}
.site-header{left:0;top:0;width:1200px;height:143px;background:var(--white)}
.brand{left:143px;top:62px;font-size:24px;font-weight:700;color:var(--orange);display:flex;align-items:center;gap:10px}
.brand .mark{width:20px;height:20px;border-radius:50%;background:var(--orange)}
.contact-line{right:144px;top:28px;display:flex;gap:34px;font-size:27px;color:var(--text)}
.contact-line span{display:flex;align-items:center;gap:10px}
.main-nav{right:144px;top:92px;display:flex;gap:31px;font-size:16px}
.main-nav a{color:var(--text);text-decoration:none}
.main-nav a.active{color:var(--orange-light)}
.service-bar{left:0;top:143px;width:1200px;height:40px;background:var(--orange);display:flex;padding-left:53px;font-size:12.5px}
.service-bar a{color:var(--white);text-decoration:none;padding:0 12px;line-height:40px}
.service-bar a.active{background:var(--orange-light)}
.hero{left:0;top:183px;width:1200px;height:530px;overflow:hidden}
.hero-photo{width:100%;height:100%;background:linear-gradient(180deg,#2d63b5 0%,#4a7dc6 45%,#3a3a3c 75%,#242424 100%)}
.hero-title{left:140px;top:40px;font-size:41px;font-weight:700;line-height:41px;color:var(--hero-title)}
.arrow{width:40px;height:40px;border-radius:50%;background:#222;top:196px;display:flex;align-items:center;justify-content:center}
.hero-curve{left:0;bottom:0}
.about-photo{left:143px;top:788px;width:437px;height:340px;background:linear-gradient(135deg,#c6d6e4,#e7e4dc 60%,#b8ad98)}
.about-copy{left:620px;top:783px;width:440px}
.about-copy h2{font-size:24px;line-height:32px;color:var(--orange);font-weight:700;margin-bottom:14px}
.about-copy p{font-size:15px;line-height:22px;margin-bottom:13px}
.about-copy li{list-style:none;font-size:14.5px;display:flex;align-items:center;gap:12px;height:40px}
.tick{width:14px;height:14px;border-radius:50%;background:var(--orange);display:inline-flex;align-items:center;justify-content:center}
.orange-band{left:0;width:1200px;background:linear-gradient(180deg,var(--orange-light),var(--orange))}
.section-title{width:1200px;left:0;text-align:center;font-size:41px;font-weight:700}
.services .section-title,.testimonials .section-title{color:var(--white)}
.service-card{width:218px;height:175px;background:var(--white);border-radius:3px;text-align:center;padding-top:18px;font-size:19px;line-height:24px;color:var(--text)}
.service-card svg{display:block;margin:0 auto 10px}
.gallery-tile{width:298px;height:191px}
.btn{background:var(--orange);color:var(--white);font-size:16px;font-weight:700;width:96px;height:39px;line-height:39px;text-align:center;border-radius:2px}
.testimonial-card{left:143px;top:2580px;width:913px;height:281px;background:var(--white);border-radius:3px;text-align:center;padding:26px 24px}
.testimonial-card h3{font-size:16px;font-weight:700;margin-bottom:12px}
.testimonial-card p{font-size:13px;line-height:26px;color:var(--muted)}
.testimonial-card .author{color:var(--orange);font-size:15px;margin-top:8px}
.contact-section{left:0;top:2943px;width:1200px;height:446px;background:radial-gradient(ellipse at 30% 40%,#f4f4f4,#dcdcdc 70%,#cfcfcf)}
.field{background:var(--white);border:1px solid #d8d8d8;font-size:13px;color:#666;padding:12px 14px}
.site-footer{left:0;top:3389px;width:1200px;height:297px;background:var(--dark)}
.footer-brand{left:143px;top:68px;font-size:20px;font-weight:700;color:var(--footer-text)}
.footer-contact{left:0;width:1200px;top:50px;text-align:center;font-size:25px;line-height:36px;color:var(--footer-text)}
.social{top:50px;width:48px;height:48px;border:1.5px solid var(--footer-text);border-radius:50%;display:flex;align-items:center;justify-content:center}
.footer-rule{left:143px;top:143px;width:913px;height:1px;background:#3a3a3a}
.footer-links{left:0;width:1200px;text-align:center;font-size:11px;color:var(--footer-text);line-height:24px}
</style>
</head>
<body>

<header class="abs site-header">
  <div class="abs brand"><span class="mark"></span>Haven &amp; Clear</div>
  <div class="abs contact-line">
    <span><svg width="26" height="20" viewBox="0 0 26 20"><rect x="1" y="1" width="24" height="18" rx="2" fill="#222"/><path d="M2 3l11 8 11-8" stroke="#fff" stroke-width="2" fill="none"/></svg>info@havenandclear.com</span>
    <span><svg width="22" height="22" viewBox="0 0 24 24"><path d="M6.6 10.8a15 15 0 006.6 6.6l2.2-2.2c.3-.3.7-.4 1-.2 1.1.4 2.3.6 3.6.6.6 0 1 .4 1 1V20c0 .6-.4 1-1 1A17 17 0 013 4c0-.6.4-1 1-1h3.5c.6 0 1 .4 1 1 0 1.3.2 2.5.6 3.6.1.3 0 .7-.2 1z" fill="#222"/></svg>0400 555 182</span>
  </div>
  <nav class="abs main-nav">
    <a class="active" href="#">HOME</a><a href="#">ABOUT</a><a href="#">TESTIMONIALS</a><a href="#">CONTACT US</a>
  </nav>
</header>

<nav class="abs service-bar">
  <a class="active" href="#">Fire &amp; Smoke Restoration</a><a href="#">Water Restoration</a><a href="#">Mould Remediation</a><a href="#">Crime Scene Cleaners</a><a href="#">Methamphetamine Remediation</a><a href="#">Testing Services</a><a href="#">Hoarding &amp; Squalor Cleaning</a>
</nav>

<section class="abs hero">
  <div class="hero-photo" role="img" aria-label="Cleaners in white protective suits clearing a fire-damaged roof under a blue sky"></div>
  <h1 class="abs hero-title">FIRE &amp; SMOKE<br>RESTORATION</h1>
  <div class="abs arrow" style="left:54px"><svg width="14" height="14" viewBox="0 0 14 14"><path d="M9 2L4 7l5 5" stroke="#fff" stroke-width="2.4" fill="none"/></svg></div>
  <div class="abs arrow" style="left:1102px"><svg width="14" height="14" viewBox="0 0 14 14"><path d="M5 2l5 5-5 5" stroke="#fff" stroke-width="2.4" fill="none"/></svg></div>
  <svg class="abs hero-curve" width="1200" height="120" viewBox="0 0 1200 120">
    <path d="M0 40 Q560 160 1200 40 L1200 120 L0 120Z" fill="#fff"/>
    <path d="M0 40 Q560 160 1200 40 L1200 48 Q560 170 0 48Z" fill="var(--orange)"/>
  </svg>
</section>

<section class="about">
  <div class="abs about-photo" role="img" aria-label="Cleaner spraying and mopping a hospital floor"></div>
  <div class="abs about-copy">
    <h2>WE ARE SPECIALISES IN ALL FORENSIC &amp; TRAUMA CLEANING, DOMESTIC AND COMMERCIAL CLEANING.</h2>
    <p>A team of experienced and quality driven cleaners, we pride ourselves on :</p>
    <ul>
      <li><span class="tick"><svg width="8" height="8" viewBox="0 0 8 8"><path d="M1 4l2 2 4-4" stroke="#fff" stroke-width="1.5" fill="none"/></svg></span>Providing the best clean</li>
      <li><span class="tick"><svg width="8" height="8" viewBox="0 0 8 8"><path d="M1 4l2 2 4-4" stroke="#fff" stroke-width="1.5" fill="none"/></svg></span>Attention to detail</li>
      <li><span class="tick"><svg width="8" height="8" viewBox="0 0 8 8"><path d="M1 4l2 2 4-4" stroke="#fff" stroke-width="1.5" fill="none"/></svg></span>Customer satisfaction</li>
      <li><span class="tick"><svg width="8" height="8" viewBox="0 0 8 8"><path d="M1 4l2 2 4-4" stroke="#fff" stroke-width="1.5" fill="none"/></svg></span>Friendly service and listening to the needs of our customers</li>
      <li><span class="tick"><svg width="8" height="8" viewBox="0 0 8 8"><path d="M1 4l2 2 4-4" stroke="#fff" stroke-width="1.5" fill="none"/></svg></span>A competitive price for the best quality service</li>
    </ul>
  </div>
</section>

<section class="abs orange-band services" style="top:1208px;height:572px">
  <h2 class="abs section-title" style="top:70px">OUR SERVICES</h2>
  <div class="abs service-card" style="left:143px;top:130px"><svg width="60" height="70" viewBox="0 0 60 70" fill="none" stroke="#222" stroke-width="2"><path d="M30 4C34 20 50 28 50 46a20 20 0 01-40 0c0-10 6-16 10-22 2 8 6 10 6 10 0-12 4-22 4-30z"/><path d="M30 40c4 6 8 8 8 14a8 8 0 01-16 0c0-6 6-8 8-14z"/></svg>Fire &amp; Smoke<br>Restoration</div>
  <div class="abs service-card" style="left:375px;top:130px"><svg width="74" height="70" viewBox="0 0 74 70" fill="none" stroke="#222" stroke-width="2"><path d="M14 48V28L37 10l23 18v20"/><rect x="30" y="32" width="14" height="16"/><path d="M4 54q6-5 11 0t11 0 11 0 11 0 11 0 11 0M4 62q6-5 11 0t11 0 11 0 11 0 11 0 11 0"/></svg>Water Restoration</div>
  <div class="abs service-card" style="left:607px;top:130px"><svg width="70" height="70" viewBox="0 0 70 70" fill="none" stroke="#222" stroke-width="2"><circle cx="33" cy="33" r="17"/><circle cx="28" cy="29" r="4"/><circle cx="39" cy="38" r="3"/><path d="M33 8v8M33 50v8M8 33h8M50 33h8M15 15l6 6M45 45l6 6M51 15l-6 6M15 51l6-6"/></svg>Mould Remediation</div>
  <div class="abs service-card" style="left:839px;top:130px"><svg width="70" height="70" viewBox="0 0 70 70" fill="none" stroke="#222" stroke-width="2"><rect x="10" y="4" width="50" height="64"/><rect x="17" y="10" width="36" height="52"/><path d="M10 24l50 10M10 40l50-8M10 52l50 8"/></svg>Crime Scene<br>Cleaners</div>
  <div class="abs service-card" style="left:260px;top:320px"><svg width="70" height="70" viewBox="0 0 70 70" fill="none" stroke="#222" stroke-width="2"><rect x="20" y="6" width="20" height="12"/><rect x="14" y="18" width="32" height="46"/><rect x="46" y="30" width="14" height="34" rx="4"/><path d="M22 30h16M22 40h16M22 50h16"/></svg>Methamphetamine<br>Remediation</div>
  <div class="abs service-card" style="left:491px;top:320px"><svg width="70" height="70" viewBox="0 0 70 70" fill="none" stroke="#222" stroke-width="2"><path d="M10 6q20 20 0 40t0 20M30 6q-20 20 0 40t0 20M12 16h16M12 36h16M12 56h16"/><path d="M46 10l10 24M40 62h26M52 34a10 10 0 01-4 22"/></svg>Testing Services</div>
  <div class="abs service-card" style="left:723px;top:320px"><svg width="84" height="70" viewBox="0 0 84 70" fill="none" stroke="#222" stroke-width="2"><path d="M6 20h72v40H6zM6 20l6-12h60l6 12"/><path d="M16 8v12M26 8v12M36 8v12M46 8v12M56 8v12M66 8v12"/><rect x="14" y="34" width="18" height="14"/><circle cx="58" cy="48" r="10"/></svg>Hoarding &amp; Squalor<br>Cleaning</div>
</section>

<section class="gallery">
  <h2 class="abs section-title" style="top:1848px;color:var(--orange)">GALLERY</h2>
  <div class="abs gallery-tile" style="left:143px;top:1913px;background:linear-gradient(135deg,#e9e5dc,#b8b3a6)" role="img" aria-label="Water-damaged ceiling with peeling plaster over pipes"></div>
  <div class="abs gallery-tile" style="left:451px;top:1913px;background:linear-gradient(90deg,#6b5542,#a68f74 50%,#e9e2d6 51%,#f2ede4)" role="img" aria-label="Room shown before and after restoration"></div>
  <div class="abs gallery-tile" style="left:759px;top:1913px;background:linear-gradient(180deg,#4b4744,#6e6a63 50%,#7fb1b8)" role="img" aria-label="Flooded dining room"></div>
  <div class="abs gallery-tile" style="left:143px;top:2114px;background:linear-gradient(135deg,#2a2520,#8a7552 55%,#c8b894)" role="img" aria-label="Smoke-blackened ceiling and walls"></div>
  <div class="abs gallery-tile" style="left:451px;top:2114px;background:linear-gradient(135deg,#c8cfd8,#8f9aa8 60%,#b6ad94)" role="img" aria-label="Worker in protective suit treating mould on a wall"></div>
  <div class="abs gallery-tile" style="left:759px;top:2114px;background:linear-gradient(135deg,#e7e3d8,#8fa4c0 60%,#5d6f93)" role="img" aria-label="Peeling ceiling paint after water damage"></div>
  <div class="abs btn" style="left:552px;top:2331px">VIEW ALL</div>
</section>

<section class="abs orange-band testimonials" style="top:2450px;height:493px">
  <h2 class="abs section-title" style="top:62px">TESTIMONIALS</h2>
</section>
<div class="abs testimonial-card">
  <h3>DOMESTIC</h3>
  <p>“ Our experience of Pieter Van Dorn has been excellent. Which is just as well because between having an 18 month old son and both of us working we needed a little help around the house. We went through several cleaners over a year or so, before finding Pieter Van Dorn. They have been helping us keep the house clean and tidy for the last year now. We are very happy with both the quality of the work and the cost is reasonable. We have also come to trust our cleaners and feel comfortable recommending the cleaning service provided by Pieter Van Dorn. ”</p>
  <div class="author">Jonah &amp; Elise Marsh - Maple Ridge</div>
  <div class="btn" style="margin:18px auto 0">VIEW ALL</div>
</div>

<section class="abs contact-section">
  <h2 class="abs section-title" style="top:70px;color:var(--orange)">CONTACT US</h2>
  <div class="abs field" style="left:143px;top:132px;width:298px;height:39px">Name</div>
  <div class="abs field" style="left:451px;top:132px;width:298px;height:39px">Email</div>
  <div class="abs field" style="left:759px;top:132px;width:297px;height:39px">Phone</div>
  <div class="abs field" style="left:143px;top:188px;width:913px;height:112px">Message</div>
  <div class="abs btn" style="left:552px;top:323px">SUBMIT</div>
</section>

<footer class="abs site-footer">
  <div class="abs footer-brand">Haven &amp; Clear</div>
  <div class="abs footer-contact">0400 555 182<br>info@havenandclear.com</div>
  <div class="abs social" style="left:879px"></div>
  <div class="abs social" style="left:943px"></div>
  <div class="abs social" style="left:1008px"><svg width="20" height="15" viewBox="0 0 20 15"><rect x="1" y="1" width="18" height="13" rx="1.5" fill="var(--footer-text)"/><path d="M2 2l8 6 8-6" stroke="#1d1d1d" stroke-width="1.5" fill="none"/></svg></div>
  <div class="abs footer-rule"></div>
  <div class="abs footer-links" style="top:180px">Home &nbsp;| &nbsp;About Fire &amp; Smoke Restoration &nbsp;| &nbsp;Water Restoration &nbsp;| &nbsp;Mould Remediation &nbsp;| &nbsp;Crime Scene Cleaners &nbsp;| &nbsp;Methamphetamine Remediation<br>Testing Services &nbsp;| &nbsp;Hoarding &amp; Squalor Cleaning &nbsp;| &nbsp;Testimonials &nbsp;| &nbsp;Contact Us</div>
  <div class="abs footer-links" style="top:242px">Copyright © 2020 &nbsp;Haven &amp; Clear Services. &nbsp;All rights reserved.</div>
</footer>

</body>
</html>
```